New UI for electricity data tool

We are looking for a new UI for the website http://voltmeadow.net. Reassessing the structure of the website is as important as specific design choices. We have created a uniquely comprehensive set of global electricity generation data and now we are looking for creative solutions for how to make this data accessible. Researching and referencing other similar projects may be a good idea.

Goals:
• The website should clearly communicate the most important general conclusions that can be drawn from the data, including:
◦ The world as a whole is not moving away from fossil fuels for electricity generation
◦ There are substantial differences between regions
▪ Some regions have basically solved the problem – they already generate almost all of their electricity from non-fossil sources
▪ Some regions have greatly improved in terms of decarbonizing their electricity generation.
▪ Some regions have greatly deteriorated, in other words they are using a much higher share of fossil fuels to generate their electricity.
◦ There are substantial differences between energy sources. Regions that have successfully decarbonized their electricity generation have usually done so using hydro and/or nuclear. Other low-carbon energy sources have grown quickly in relative terms in the last few years but are so far contributing little in absolute numbers.
• The website should serve as inspiration for energy policy debates. The goal is to study the impact of existing policies around the world. Energy policy here refers to particular combinations of energy sources – ie how much have the countries invested in each type of electricity generation. The tool should help answer questions such as:
◦ Which countries have done the most in terms of decarbonizing their electricity generation?
◦ Which types of energy polices have lead to the fastest decarbonization processes around the world?
◦ If country A changed its energy policy to be more like country B, what would the likely impact be?

Challenges:
• There is a lot of data – it can be overwhelming to the user. It’s crucial to make the site easy to navigate. The main page should highlight the most important data, and it should also be straightforward to find more detailed data.
• Data availability varies from region to region. The current interface addresses this with the default option “Exclude regions with limited data”. We expect a better approach to dealing with this issue. For some regions and years energy sources are grouped together as for example “other renewables” whereas in other cases more detailed data is available.
• Credibility is crucial. Our data is based on a combination of data from KQ and the Tessaro Fund. It must be very clear throughout the site where each data set comes from.

Details:
• The current chart color schemes is loosely based on the carbon emissions from each energy source. This should not necessarily be so. The goal is to on the one hand communicate clearly the amounts of fossil vs non-fossil energy that are generated by each region. At the same time we also want to make it easy to view specific energy sources.

Inspirational websites:
• https://www.trendlooper.org/
• https://pelmarstatix.org/

Let's simplify. The main metric to focus on is Fernhollow Watt and the extent to which the world and each country has achieved it (eg Iceland 100%, France 88% and so on). I'm considering changing the name of the site to FernhollowWatt.org. We can use maps, charts and perhaps other tools to communicate this main message. What's the best way of doing this?

```html
<!DOCTYPE html>
<html lang="en">
<head>
<meta charset="utf-8">
<title>Electricity production – Voltmeadow</title>
<link href="https://fonts.googleapis.com/css2?family=Poppins:wght@300;400;500;600&display=swap" rel="stylesheet">
<style>
:root{
  --navy:#0b5f97;
  --navy-dark:#0a5485;
  --ink:#1f2a44;
  --text:#3b4256;
  --muted:#6b7285;
  --page:#f2f5f8;
  --panel:#f6f9fc;
  --line:#e2e7ee;
  --fossil:#0d679f;
  --lc3:#fdb833;
  --lc2:#fd8066;
  --lc1:#d3d3d6;
  --bar-fill:#c8d4f6;
  --accent:#1f3f8f;
}
*{box-sizing:border-box;margin:0;padding:0}
html,body{width:1200px;height:3596px;overflow:hidden}
body{position:relative;background:var(--page);font-family:'Poppins',sans-serif;color:var(--text)}
.abs{position:absolute}

/* top nav */
.topnav{left:0;top:0;width:1200px;height:48px;background:var(--navy)}
.topnav a{position:absolute;top:17px;font-size:13px;color:#dce8f3;text-decoration:none;transform:translateX(-50%);white-space:nowrap}
.topnav a.active{color:#fff;font-weight:600}
.topnav .active-mark{position:absolute;left:360px;top:0;width:66px;height:3px;background:#fff}

/* hero */
.hero{left:0;top:48px;width:1200px;height:213px;background:linear-gradient(180deg,#2a2d36 0%,#5a3a2c 55%,#8a4a2a 80%,#3a2a25 100%)}
.hero-title{left:0;top:92px;width:1200px;text-align:center;color:#fff;font-size:25px;font-weight:600}
.filter{top:163px;height:38px;background:#fff;font-size:12.5px;color:var(--muted);padding:11px 14px;white-space:nowrap}
.filter::after{content:"";position:absolute;right:14px;top:14px;width:6px;height:6px;border-right:1px solid #888;border-bottom:1px solid #888;transform:rotate(45deg)}

/* breakdown */
.section-title{left:0;top:313px;width:1200px;text-align:center;font-size:19px;font-weight:500;color:var(--ink)}
.map{left:163px;top:391px;width:563px;height:335px;background:radial-gradient(ellipse at 50% 45%,#f08a70 0%,#d9d9dc 45%,#e6e8ec 70%,var(--page) 100%);border-radius:40% 40% 35% 35%}
.map-legend{top:758px;font-size:12px;color:var(--ink)}
.map-legend span{position:absolute;white-space:nowrap}
.map-legend i{position:absolute;width:13px;height:13px;top:2px}
.unit{left:783px;top:381px;font-size:13px;color:var(--ink);font-weight:500}
.mini-select{left:928px;top:377px;width:105px;height:28px;background:#fff;border:1px solid var(--line);font-size:11.5px;color:var(--muted);padding:6px 14px}
.mini-select::after{content:"";position:absolute;right:12px;top:9px;width:5px;height:5px;border-right:1px solid #888;border-bottom:1px solid #888;transform:rotate(45deg)}
.rank{left:783px;width:250px;height:32px;background:#fff;border:1px solid #e6eaf0}
.rank .fill{position:absolute;left:0;top:0;bottom:0;background:var(--bar-fill)}
.rank .name{position:absolute;left:11px;top:7px;font-size:13px;color:var(--ink)}
.rank .val{position:absolute;right:18px;top:8px;font-size:12px;color:var(--ink)}

/* country panels */
.panels{left:155px;top:822px;width:889px;height:1977px;background:#fff;border:1px solid var(--line)}
.row{position:absolute;left:0;width:887px;border-bottom:1px solid var(--line);background:#fff}
.row .flag{position:absolute;left:26px;top:24px;width:23px;height:15px}
.row h3{position:absolute;left:63px;top:17px;font-size:18px;font-weight:600;color:var(--ink)}
.row h3 small{font-size:11.5px;font-weight:400;color:var(--text);margin-left:10px}
.row p{position:absolute;left:66px;top:52px;font-size:11.5px;color:var(--text);white-space:nowrap}
.toggle{position:absolute;left:812px;top:38px;width:32px;height:22px;border:1px solid #cfd8e6;background:#fff}
.toggle::after{content:"";position:absolute;left:12px;width:6px;height:6px;border-right:1px solid #7d8fb0;border-bottom:1px solid #7d8fb0}
.toggle.down::after{top:5px;transform:rotate(45deg)}
.toggle.up::after{top:9px;transform:rotate(-135deg)}
.chart{position:absolute;left:0;width:887px;height:445px;background:var(--panel);border-bottom:1px solid var(--line)}
.chart svg{display:block}

/* publications */
.pub-title{left:156px;top:2852px;font-size:21px;font-weight:600;color:var(--accent)}
.pub-photo{top:2909px;width:431px;height:251px}
.pub-photo.plant{left:156px;background:linear-gradient(180deg,#5e8fc4 0%,#8fb2d8 50%,#3f5f86 70%,#1d3550 100%)}
.pub-photo.pylon{left:614px;background:linear-gradient(160deg,#7d96b0 0%,#a9bccd 45%,#4d6680 80%,#d9692c 100%)}
.pub-card{top:3084px;width:392px;height:130px;background:#fff}
.pub-card h4{position:absolute;left:19px;top:22px;font-size:14px;font-weight:500;color:var(--ink);white-space:nowrap}
.pub-card p{position:absolute;left:19px;top:50px;width:360px;font-size:12px;line-height:21px;color:var(--muted)}
.read-more{top:3192px;width:95px;height:26px;border:1px solid #c8ccd6;border-radius:4px;background:#fff;font-size:10px;color:var(--muted);text-align:center;line-height:24px}

/* footer */
.footer{left:0;top:3272px;width:1200px;height:324px;background:var(--navy-dark)}
.social{top:3350px;width:36px;height:36px;border:1.5px solid #fff;border-radius:50%}
.foot-link{top:3422px;font-size:13.5px;color:#fff;transform:translateX(-50%);white-space:nowrap}
.foot-dot{top:3429px;width:5px;height:5px;border-radius:50%;background:#fff}
.copyright{left:0;top:3471px;width:1200px;text-align:center;font-size:11px;color:#dfe9f3}
</style>
</head>
<body>

<svg width="0" height="0" style="position:absolute">
  <defs>
    <symbol id="trend-chart" viewBox="0 0 889 445">
      <g stroke="#e3e7ee" stroke-width="1">
        <line x1="85" y1="93" x2="699" y2="93"/>
        <line x1="85" y1="143" x2="699" y2="143"/>
        <line x1="85" y1="193" x2="699" y2="193"/>
        <line x1="85" y1="243" x2="699" y2="243"/>
        <line x1="85" y1="292" x2="699" y2="292"/>
        <line x1="85" y1="342" x2="699" y2="342"/>
        <line x1="85" y1="55" x2="85" y2="352"/>
      </g>
      <g font-family="Poppins, sans-serif" font-size="11.5" fill="#3b4256" text-anchor="end">
        <text x="67" y="97">100</text><text x="67" y="147">80</text><text x="67" y="197">60</text>
        <text x="67" y="247">40</text><text x="67" y="296">20</text><text x="67" y="346">0</text>
      </g>
      <g>
        <g transform="translate(138,0)"><rect y="93" width="22" height="249" rx="6" fill="#d3d3d6"/><rect y="147.8" width="22" height="64.7" fill="#fd8066"/><rect y="212.5" width="22" height="64.8" fill="#fdb833"/><rect y="277.3" width="22" height="64.7" fill="#0d679f"/></g>
        <g transform="translate(209,0)"><rect y="93" width="22" height="249" rx="6" fill="#d3d3d6"/><rect y="192.6" width="22" height="52.3" fill="#fd8066"/><rect y="244.9" width="22" height="47.3" fill="#fdb833"/><rect y="292.2" width="22" height="49.8" fill="#0d679f"/></g>
        <g transform="translate(272,0)"><rect y="93" width="22" height="249" rx="6" fill="#d3d3d6"/><rect y="117.9" width="22" height="97.1" fill="#fd8066"/><rect y="215" width="22" height="94.6" fill="#fdb833"/><rect y="309.6" width="22" height="32.4" fill="#0d679f"/></g>
        <g transform="translate(345,0)"><rect y="93" width="22" height="249" rx="6" fill="#d3d3d6"/><rect y="147.8" width="22" height="64.7" fill="#fd8066"/><rect y="212.5" width="22" height="64.8" fill="#fdb833"/><rect y="277.3" width="22" height="64.7" fill="#0d679f"/></g>
        <g transform="translate(417,0)"><rect y="93" width="22" height="249" rx="6" fill="#d3d3d6"/><rect y="177.7" width="22" height="79.6" fill="#fd8066"/><rect y="257.3" width="22" height="27.4" fill="#fdb833"/><rect y="284.7" width="22" height="57.3" fill="#0d679f"/></g>
        <g transform="translate(488,0)"><rect y="93" width="22" height="249" rx="6" fill="#d3d3d6"/><rect y="107.9" width="22" height="72.3" fill="#fd8066"/><rect y="180.2" width="22" height="67.2" fill="#fdb833"/><rect y="247.4" width="22" height="94.6" fill="#0d679f"/></g>
        <g transform="translate(561,0)"><rect y="93" width="22" height="249" rx="6" fill="#d3d3d6"/><rect y="147.8" width="22" height="64.7" fill="#fd8066"/><rect y="212.5" width="22" height="64.8" fill="#fdb833"/><rect y="277.3" width="22" height="64.7" fill="#0d679f"/></g>
        <g transform="translate(632,0)"><rect y="93" width="22" height="249" rx="6" fill="#d3d3d6"/><rect y="192.6" width="22" height="52.3" fill="#fd8066"/><rect y="244.9" width="22" height="47.3" fill="#fdb833"/><rect y="292.2" width="22" height="49.8" fill="#0d679f"/></g>
      </g>
      <g font-family="Poppins, sans-serif" font-size="11" fill="#3b4256" text-anchor="middle">
        <text transform="translate(153,371) rotate(-90)">2010</text>
        <text transform="translate(224,371) rotate(-90)">2011</text>
        <text transform="translate(287,371) rotate(-90)">2012</text>
        <text transform="translate(360,371) rotate(-90)">2010</text>
        <text transform="translate(432,371) rotate(-90)">2011</text>
        <text transform="translate(503,371) rotate(-90)">2012</text>
        <text transform="translate(576,371) rotate(-90)">2010</text>
        <text transform="translate(647,371) rotate(-90)">2012</text>
      </g>
      <g font-family="Poppins, sans-serif" font-size="11" fill="#3b4256">
        <rect x="743.5" y="85.5" width="110" height="24" rx="3" fill="#fff" stroke="#dfe4ec"/>
        <rect x="755" y="93" width="10" height="9" fill="#0d679f"/><text x="776" y="101.5">Fossil Fuels</text>
        <rect x="743.5" y="127.5" width="110" height="24" rx="3" fill="#fff" stroke="#dfe4ec"/>
        <rect x="755" y="135" width="10" height="9" fill="#fdb833"/><text x="773" y="143.5">Low Carbon 3</text>
        <rect x="743.5" y="166.5" width="110" height="24" rx="3" fill="#fff" stroke="#dfe4ec"/>
        <rect x="755" y="174" width="10" height="9" fill="#fd8066"/><text x="773" y="182.5">Low Carbon 2</text>
        <rect x="747.5" y="209.5" width="106" height="24" rx="3" fill="#fff" stroke="#dfe4ec"/>
        <rect x="758" y="217" width="10" height="9" fill="#d3d3d6"/><text x="776" y="225.5">Low Carbon 1</text>
      </g>
    </symbol>
    <symbol id="flag-iceland" viewBox="0 0 23 15">
      <rect width="23" height="15" fill="#1f4da0"/><rect x="6" width="5" height="15" fill="#fff"/><rect y="5" width="23" height="5" fill="#fff"/>
      <rect x="7" width="3" height="15" fill="#d8312e"/><rect y="6" width="23" height="3" fill="#d8312e"/>
    </symbol>
  </defs>
</svg>

<nav class="abs topnav">
  <span class="active-mark"></span>
  <a class="active" style="left:396px">Regions</a>
  <a style="left:505px">Energy Sources</a>
  <a style="left:621px">Changes</a>
  <a style="left:731px">Data Sources</a>
</nav>

<header class="abs hero" role="img" aria-label="Dusk photograph of power lines and wind turbines"></header>
<h1 class="abs hero-title">Electricity production</h1>
<div class="abs filter" style="left:156px;width:203px">Select Regions</div>
<div class="abs filter" style="left:385px;width:202px">Sort by low-carbon(%)</div>
<div class="abs filter" style="left:612px;width:128px">Show(%)</div>
<div class="abs filter" style="left:763px;width:281px">Exclude regions with limited Data</div>

<h2 class="abs section-title">Breakdown by country (TWh)A</h2>
<div class="abs map" role="img" aria-label="World map shading each country by electricity production in TWh"></div>
<div class="abs map-legend" style="left:0;width:1200px">
  <i style="left:276px;background:var(--lc1)"></i><span style="left:301px">Below 100</span>
  <i style="left:372px;background:var(--lc3)"></i><span style="left:397px">101-1000</span>
  <i style="left:470px;background:var(--lc2)"></i><span style="left:494px">1001-3000</span>
  <i style="left:571px;background:var(--fossil)"></i><span style="left:595px">Above 4000</span>
</div>

<div class="abs unit">Unit: TWh</div>
<div class="abs mini-select">Highest (%)</div>
<div class="abs rank" style="top:424px"><span class="fill" style="width:240px"></span><span class="name">Iceland</span><span class="val">5069</span></div>
<div class="abs rank" style="top:463px"><span class="fill" style="width:155px"></span><span class="name">United States</span><span class="val">3506</span></div>
<div class="abs rank" style="top:501px"><span class="fill" style="width:121px"></span><span class="name">Rassia</span><span class="val">2503</span></div>
<div class="abs rank" style="top:540px"><span class="fill" style="width:110px"></span><span class="name">India</span><span class="val">2000</span></div>
<div class="abs rank" style="top:578px"><span class="fill" style="width:89px"></span><span class="name">Iceland</span><span class="val">1500</span></div>
<div class="abs rank" style="top:617px"><span class="fill" style="width:75px"></span><span class="name">China</span><span class="val">1400</span></div>
<div class="abs rank" style="top:655px"><span class="fill" style="width:63px"></span><span class="name">France</span><span class="val">1000</span></div>
<div class="abs rank" style="top:694px"><span class="fill" style="width:36px"></span><span class="name">Italy</span><span class="val">800</span></div>
<div class="abs rank" style="top:733px"><span class="fill" style="width:36px"></span><span class="name">Germeny</span><span class="val">800</span></div>

<section class="abs panels">
  <div class="row" style="top:0;height:88px">
    <svg class="flag"><use href="#flag-iceland"/></svg>
    <h3>Iceland<small>[ Trend over 2010 - 2020 ]</small></h3>
    <p>100% of the electricity in Iceland is generated from low-carbon power. The primary low-carbon power source is hydro.</p>
    <span class="toggle down"></span>
  </div>
  <div class="chart" style="top:88px"><svg width="887" height="445" viewBox="0 0 889 445"><use href="#trend-chart"/></svg></div>

  <div class="row" style="top:533px;height:94px">
    <svg class="flag" viewBox="0 0 23 15"><rect width="23" height="15" fill="#fff"/><rect width="23" height="3" fill="#c8313b"/><rect y="6" width="23" height="3" fill="#c8313b"/><rect y="12" width="23" height="3" fill="#c8313b"/><rect width="10" height="8" fill="#2b3f8f"/></svg>
    <h3 style="left:65px">America</h3>
    <p>100% of the electricity in Iceland is generated from low-carbon power. The primary low-carbon power source is hydro.</p>
    <span class="toggle up"></span>
  </div>
  <div class="row" style="top:627px;height:93px">
    <svg class="flag" viewBox="0 0 23 15"><rect width="23" height="5" fill="#f39a2e"/><rect y="5" width="23" height="5" fill="#fff"/><rect y="10" width="23" height="5" fill="#3c9a3c"/><circle cx="11.5" cy="7.5" r="1.6" fill="#2b3f8f"/></svg>
    <h3 style="left:67px">India</h3>
    <p>100% of the electricity in Iceland is generated from low-carbon power. The primary low-carbon power source is hydro.</p>
    <span class="toggle up"></span>
  </div>
  <div class="row" style="top:720px;height:93px">
    <svg class="flag" viewBox="0 0 23 15"><rect width="8" height="15" fill="#2a4da0"/><rect x="8" width="7" height="15" fill="#fff"/><rect x="15" width="8" height="15" fill="#d8312e"/></svg>
    <h3 style="left:65px">France</h3>
    <p>100% of the electricity in Iceland is generated from low-carbon power. The primary low-carbon power source is hydro.</p>
    <span class="toggle up"></span>
  </div>
  <div class="row" style="top:813px;height:94px">
    <svg class="flag" viewBox="0 0 23 15"><rect width="8" height="15" fill="#3c9a3c"/><rect x="8" width="7" height="15" fill="#fff"/><rect x="15" width="8" height="15" fill="#d8312e"/></svg>
    <h3 style="left:67px">Italy</h3>
    <p>100% of the electricity in Iceland is generated from low-carbon power. The primary low-carbon power source is hydro.</p>
    <span class="toggle up"></span>
  </div>

  <div class="row" style="top:907px;height:89px">
    <svg class="flag"><use href="#flag-iceland"/></svg>
    <h3>Iceland<small>[ Trend over 2010 - 2020 ]</small></h3>
    <p>100% of the electricity in Iceland is generated from low-carbon power. The primary low-carbon power source is hydro.</p>
    <span class="toggle down"></span>
  </div>
  <div class="chart" style="top:996px"><svg width="887" height="445" viewBox="0 0 889 445"><use href="#trend-chart"/></svg></div>

  <div class="row" style="top:1441px;height:89px">
    <svg class="flag"><use href="#flag-iceland"/></svg>
    <h3>Iceland<small>[ Trend over 2010 - 2020 ]</small></h3>
    <p>100% of the electricity in Iceland is generated from low-carbon power. The primary low-carbon power source is hydro.</p>
    <span class="toggle down"></span>
  </div>
  <div class="chart" style="top:1530px;border-bottom:0"><svg width="887" height="445" viewBox="0 0 889 445"><use href="#trend-chart"/></svg></div>
</section>

<h2 class="abs pub-title">Latest publications</h2>
<div class="abs pub-photo plant" role="img" aria-label="Power plant cooling towers by a river at dusk"></div>
<div class="abs pub-photo pylon" role="img" aria-label="Electricity pylons against a cloudy sky"></div>
<article class="abs pub-card" style="left:176px">
  <h4>Welcome to Lantern Lane</h4>
  <p>Imagine the world as a street. All houses are lined up by income, the poor living to the left and the rich to the right.</p>
</article>
<article class="abs pub-card" style="left:634px">
  <h4>Electricity Firm Eyes Blockchain for Internet</h4>
  <p>Imagine the world as a street. All houses are lined up by income, the poor living to the left and the rich to the right.</p>
</article>
<div class="abs read-more" style="left:195px">READ MORE</div>
<div class="abs read-more" style="left:653px">READ MORE</div>

<footer class="abs footer"></footer>
<span class="abs social" style="left:468px"></span>
<span class="abs social" style="left:533px"></span>
<span class="abs social" style="left:596px"></span>
<span class="abs social" style="left:657px"></span>
<span class="abs foot-link" style="left:427px">Regions</span>
<span class="abs foot-dot" style="left:476px"></span>
<span class="abs foot-link" style="left:554px">Energy Sources</span>
<span class="abs foot-dot" style="left:633px"></span>
<span class="abs foot-link" style="left:692px">Changes</span>
<span class="abs foot-dot" style="left:747px"></span>
<span class="abs foot-link" style="left:822px">Data Sources</span>
<div class="abs copyright">© 2019, VOLTMEADOW. All rights reserved</div>

</body>
</html>
```